Business card for a shipping supplies business

Needing a business card design. Please see the logo. The logo with the white font should be used if there is a dark background.

We are looking for the following info on the card. Please see the sample info. We will need the info to be changed with a few different employee names and info but all will use the same template.

Business Name: The Crate Heron
Employee Name : Marcus Delaney
Position: Account Manager
Address: 4827 W. Ridge 418 S.
Fort Worth, TX 73948
email: Marcus@thecrateheron.example
telephone: 855-619-2740 x 207
website: www.getparcelkits.example

Target Market(s)

Businesses who ship products for online sales

Industry/Entity Type

Cardboard

Contact Information for Business Card

Name, title, address, website, logo, telephone number

Font styles to use
Sans Serif

Colors
EE7325
F08F49
F5BC92
FAE3D3
FDF4ED

Requirements
Must have
• Logo on back of card. Clean look, just logo, website address

```html
<!DOCTYPE html>
<html lang="en">
<head>
<meta charset="utf-8">
<title>The Crate Heron – Business Card</title>
<link rel="stylesheet" href="https://fonts.googleapis.com/css2?family=Arimo:wght@400;700&display=swap">
<style>
  :root {
    --stage: #2b2b2b;
    --ink: #111111;
    --card-dark: #000000;
    --card-light: #ffffff;
    --orange: #EE7325;
    --orange-soft: #F08F49;
    --rule: #d8d8d8;
    --white: #ffffff;
  }
  * { box-sizing: border-box; margin: 0; padding: 0; }
  html, body {
    width: 1200px; height: 1015px; overflow: hidden;
    background: var(--stage);
    font-family: "Arimo", Arial, sans-serif;
  }
  .canvas {
    width: 1200px; height: 1015px;
    display: flex; flex-direction: column; align-items: center; justify-content: center;
    gap: 45px;
  }
  .card {
    width: 700px; height: 400px; position: relative;
    box-shadow: 0 12px 30px rgba(0,0,0,.5);
  }
  .card--front { background: var(--card-dark); }
  .card--back { background: var(--card-light); display: flex; align-items: center; }

  .brand {
    display: flex; align-items: center; gap: 14px;
    font-weight: 700; letter-spacing: .02em; text-transform: uppercase;
  }
  .brand__dot { border-radius: 50%; background: var(--orange); flex: none; }

  .card--front .brand {
    position: absolute; left: 0; right: 0; top: 0; bottom: 0;
    justify-content: center; color: var(--white); font-size: 46px;
  }
  .card--front .brand__dot { width: 34px; height: 34px; }

  .back__logo { width: 330px; display: flex; justify-content: center; }
  .card--back .brand { color: var(--ink); font-size: 27px; }
  .card--back .brand__dot { width: 20px; height: 20px; }

  .back__divider {
    width: 1px; height: 290px;
    background: linear-gradient(to bottom, transparent, var(--rule) 20%, var(--rule) 80%, transparent);
  }

  .contact { padding-left: 38px; color: var(--ink); }
  .contact__name { font-size: 26px; font-weight: 700; text-transform: uppercase; letter-spacing: .01em; line-height: 1.1; }
  .contact__name .surname { color: var(--orange); }
  .contact__title { font-size: 15px; margin-bottom: 18px; }
  .contact__list { list-style: none; font-size: 14.5px; line-height: 1.55; }
  .contact__list li { display: flex; align-items: center; gap: 8px; }
  .contact__list svg { width: 14px; height: 14px; flex: none; fill: var(--orange); }
  .accent { color: var(--orange); }
  .contact__address { font-size: 14.5px; line-height: 1.35; margin-top: 12px; padding-left: 22px; }
</style>
</head>
<body>
<main class="canvas">
  <section class="card card--front" aria-label="Card back">
    <div class="brand"><span class="brand__dot"></span>The Crate Heron</div>
  </section>

  <section class="card card--back" aria-label="Card front">
    <div class="back__logo">
      <div class="brand"><span class="brand__dot"></span>The Crate Heron</div>
    </div>
    <div class="back__divider"></div>
    <div class="contact">
      <p class="contact__name">Marcus <span class="surname">Delaney</span></p>
      <p class="contact__title">Account Manager</p>
      <ul class="contact__list">
        <li>
          <svg viewBox="0 0 24 24" aria-hidden="true"><path d="M6.6 10.8a15.1 15.1 0 0 0 6.6 6.6l2.2-2.2c.3-.3.7-.4 1-.2 1.1.4 2.3.6 3.6.6.6 0 1 .4 1 1V20c0 .6-.4 1-1 1A17 17 0 0 1 3 4c0-.6.4-1 1-1h3.5c.6 0 1 .4 1 1 0 1.2.2 2.4.6 3.6.1.3 0 .7-.2 1z"/></svg>
          855-619-2740 x 207
        </li>
        <li>
          <svg viewBox="0 0 24 24" aria-hidden="true"><path d="M2 5h20v14H2zM4 7v.5l8 5 8-5V7l-8 5z"/></svg>
          Marcus@thecrateheron.example
        </li>
        <li>
          <svg viewBox="0 0 24 24" aria-hidden="true"><path d="M12 2a10 10 0 1 0 0 20 10 10 0 0 0 0-20zm6.9 9h-3a15 15 0 0 0-1.3-5.6A8 8 0 0 1 18.9 11zM12 4c.9 1.2 1.8 3.6 1.9 7h-3.8C10.2 7.6 11.1 5.2 12 4zM9.4 5.4A15 15 0 0 0 8.1 11h-3a8 8 0 0 1 4.3-5.6zM5.1 13h3a15 15 0 0 0 1.3 5.6A8 8 0 0 1 5.1 13zM12 20c-.9-1.2-1.8-3.6-1.9-7h3.8c-.1 3.4-1 5.8-1.9 7zm2.6-1.4a15 15 0 0 0 1.3-5.6h3a8 8 0 0 1-4.3 5.6z"/></svg>
          <span>www.<span class="accent">getparcelkits</span>.example</span>
        </li>
      </ul>
      <p class="contact__address">4827 W. Ridge 418 S.<br>Fort Worth, TX 73948</p>
    </div>
  </section>
</main>
</body>
</html>
```